Beyond The Ledger Double Sided DL Flyer

We need a double sided flyer that we provide to a Real Estate agent for leeds. It should provide our basic services as well as a modern look and feel. The brochure should incorporate our Brand colors and have a graphic that centres around money and property. I have included a couple of pictures that we like (but have not yet purchased from PIXVAULT) as an indication of the type of picture we like.

WE need to also show the Beyond The Ledger brand and have our Phone / address's and email details.

Target Market(s)

Realestate clients (Property Investors)

Industry/Entity Type

Financial Planning

Requirements
Must have
• Picture on Front (maybe the logo on back)
• Please incorporate existing logo colours.

```html
<!DOCTYPE html>
<html lang="en">
<head>
<meta charset="utf-8">
<title>Beyond The Ledger – DL Flyer</title>
<link rel="stylesheet" href="https://fonts.googleapis.com/css2?family=Open+Sans:wght@300;400;600;700;800&display=swap">
<style>
  :root {
    --brand-green: #6ab42d;
    --brand-green-dark: #4f9a1c;
    --charcoal: #3a3a3a;
    --ink: #2e2e2e;
    --paper: #ffffff;
    --backdrop: #2a2a2a;
  }
  * { box-sizing: border-box; margin: 0; padding: 0; }
  html, body { width: 1200px; height: 1040px; overflow: hidden; }
  body {
    background: var(--backdrop);
    font-family: "Open Sans", Arial, sans-serif;
    color: var(--ink);
    position: relative;
  }
  .flyer {
    position: absolute;
    top: 40px;
    width: 480px;
    height: 960px;
    background: var(--paper);
    overflow: hidden;
  }
  .flyer--front { left: 100px; }
  .flyer--back { left: 620px; }
  .flyer svg.art { position: absolute; left: 0; top: 0; }

  /* Front */
  .front-headline {
    position: absolute;
    left: 0; right: 0; top: 690px;
    text-align: center;
    line-height: 1;
  }
  .front-headline .line { display: block; }
  .front-headline .line--lead { font-size: 41px; font-weight: 300; color: var(--ink); letter-spacing: 1px; }
  .front-headline .line--main { font-size: 50px; font-weight: 300; color: var(--ink); margin-top: 8px; }
  .front-headline .line--accent { font-size: 50px; font-weight: 300; color: var(--brand-green); margin-top: 8px; }
  .front-headline strong { font-weight: 800; }
  .front-cta {
    position: absolute;
    left: 0; right: 0; top: 855px; height: 105px;
    background: var(--charcoal);
    color: var(--paper);
    text-align: center;
    padding-top: 20px;
    font-size: 28px;
    line-height: 1.2;
  }
  .front-cta .highlight { color: var(--brand-green); font-weight: 700; }
  .front-cta .web strong { font-weight: 700; }

  /* Back */
  .brand-lockup {
    position: absolute;
    left: 0; right: 0; top: 448px;
    text-align: center;
  }
  .brand-name {
    font-size: 36px;
    font-weight: 700;
    color: var(--brand-green);
    line-height: 1;
  }
  .services-heading {
    position: absolute;
    left: 0; right: 0; top: 519px; height: 57px;
    background: var(--charcoal);
    color: var(--paper);
    text-align: center;
    font-size: 19px;
    font-weight: 600;
    line-height: 22px;
    padding-top: 6px;
  }
  .services {
    position: absolute;
    left: 38px; top: 590px;
    list-style: none;
  }
  .services li {
    display: flex;
    align-items: center;
    height: 24px;
    font-size: 14px;
    color: var(--ink);
  }
  .services svg { width: 18px; height: 16px; margin-right: 10px; }
  .contact {
    position: absolute;
    left: 24px; right: 24px; top: 798px;
    color: var(--paper);
    font-size: 15px;
    line-height: 18px;
  }
  .contact-row { display: flex; justify-content: space-between; margin-bottom: 7px; }
  .contact-item { display: flex; align-items: flex-start; }
  .contact-item svg { flex: none; margin-right: 6px; margin-top: 2px; }
  .contact-rule { border: 0; border-top: 1px solid rgba(255,255,255,0.6); margin: 12px 0 8px; }
  .contact-web { text-align: center; }
  .contact-web .email { display: flex; justify-content: center; align-items: center; font-size: 15px; }
  .contact-web .email svg { margin-right: 8px; }
  .contact-web .url { font-size: 21px; margin-top: 2px; }
  .contact-web .url strong { font-weight: 700; }
</style>
</head>
<body>

<section class="flyer flyer--front">
  <svg class="art" width="480" height="960" viewBox="0 0 480 960" aria-hidden="true">
    <path d="M0 590 Q230 720 452 540" fill="none" stroke="var(--charcoal)" stroke-width="4"/>
    <path d="M0 584 Q230 712 448 534" fill="none" stroke="var(--brand-green)" stroke-width="10"/>
    <polygon points="412,536 480,502 468,574" fill="var(--brand-green)"/>
  </svg>
  <svg class="art" width="480" height="960" viewBox="0 0 480 960" role="img" aria-label="Photo: hand watering a seedling in a coin jar beside stacked coins and a small house model on a wooden table">
    <defs>
      <linearGradient id="frontPhoto" x1="0" y1="0" x2="0" y2="1">
        <stop offset="0" stop-color="#3f7e2a"/>
        <stop offset="0.55" stop-color="#5c9a3c"/>
        <stop offset="0.75" stop-color="#8a7358"/>
        <stop offset="1" stop-color="#a0846a"/>
      </linearGradient>
    </defs>
    <path d="M0 0 H480 V520 Q420 560 400 566 Q230 660 0 570 Z" fill="url(#frontPhoto)"/>
  </svg>

  <h1 class="front-headline">
    <span class="line line--lead">LOOKING TO</span>
    <span class="line line--main"><strong>START</strong> OR <strong>GROW</strong></span>
    <span class="line line--accent">YOUR <strong>BUSINESS?</strong></span>
  </h1>

  <div class="front-cta">
    <div>Book a <span class="highlight">FREE CONSULTATION</span></div>
    <div class="web">www.<strong>btlaccounting</strong>.com.au</div>
  </div>
</section>

<section class="flyer flyer--back">
  <svg class="art" width="480" height="405" viewBox="0 0 480 405" role="img" aria-label="Photo: cupped hands holding a small wooden house behind rising coin stacks with sprouting seedlings">
    <defs>
      <linearGradient id="backPhoto" x1="0" y1="0" x2="0" y2="1">
        <stop offset="0" stop-color="#c9ccd2"/>
        <stop offset="0.5" stop-color="#ddd8d2"/>
        <stop offset="0.85" stop-color="#eeeeec"/>
        <stop offset="1" stop-color="#ffffff"/>
      </linearGradient>
    </defs>
    <rect width="480" height="405" fill="url(#backPhoto)"/>
  </svg>

  <svg class="art" width="480" height="960" viewBox="0 0 480 960" aria-hidden="true">
    <path d="M0 716 Q220 860 480 660 V960 H0 Z" fill="var(--brand-green)"/>
    <path d="M0 700 Q220 832 448 668" fill="none" stroke="var(--charcoal)" stroke-width="12"/>
    <polygon points="420,662 480,640 470,692" fill="var(--charcoal)"/>
  </svg>

  <div class="brand-lockup">
    <div class="brand-name">Beyond The Ledger</div>
  </div>

  <h2 class="services-heading">ACCOUNTANTS AND FINANCIAL ADVISORS<br>WHO SPECIALISE IN:</h2>

  <ul class="services">
    <li><svg viewBox="0 0 18 16"><path d="M1 9 L6 14 L17 1" fill="none" stroke="var(--brand-green)" stroke-width="2.4"/></svg>Negative Gearing &amp; Investment Properties</li>
    <li><svg viewBox="0 0 18 16"><path d="M1 9 L6 14 L17 1" fill="none" stroke="var(--brand-green)" stroke-width="2.4"/></svg>Property &amp; Capital Gains Tax Minimisation</li>
    <li><svg viewBox="0 0 18 16"><path d="M1 9 L6 14 L17 1" fill="none" stroke="var(--brand-green)" stroke-width="2.4"/></svg>Self-Managed Superannuation Funds (SMSF)</li>
    <li><svg viewBox="0 0 18 16"><path d="M1 9 L6 14 L17 1" fill="none" stroke="var(--brand-green)" stroke-width="2.4"/></svg>Small Business &amp; Personal Taxation</li>
    <li><svg viewBox="0 0 18 16"><path d="M1 9 L6 14 L17 1" fill="none" stroke="var(--brand-green)" stroke-width="2.4"/></svg>Investment Advice &amp; Risk Insurances</li>
  </ul>

  <div class="contact">
    <div class="contact-row">
      <div class="contact-item">
        <svg width="11" height="15" viewBox="0 0 11 15"><path d="M5.5 0 C2.5 0 0 2.4 0 5.4 C0 9 5.5 15 5.5 15 S11 9 11 5.4 C11 2.4 8.5 0 5.5 0 Z M5.5 7.5 A2 2 0 1 1 5.5 3.5 A2 2 0 1 1 5.5 7.5 Z" fill="var(--paper)"/></svg>
        <span>12 / 88 Harbour View Rd Kincumber<br>NSW 2251</span>
      </div>
      <div class="contact-item">
        <svg width="14" height="12" viewBox="0 0 14 12"><path d="M1 4 Q7 -1 13 4 L11 6 L9 4 L9 3 Q7 2 5 3 L5 4 L3 6 Z M3 7 H11 L12 11 H2 Z" fill="var(--paper)"/></svg>
        <span>(02) 5550 1234</span>
      </div>
    </div>
    <div class="contact-row">
      <div class="contact-item">
        <svg width="11" height="15" viewBox="0 0 11 15"><path d="M5.5 0 C2.5 0 0 2.4 0 5.4 C0 9 5.5 15 5.5 15 S11 9 11 5.4 C11 2.4 8.5 0 5.5 0 Z M5.5 7.5 A2 2 0 1 1 5.5 3.5 A2 2 0 1 1 5.5 7.5 Z" fill="var(--paper)"/></svg>
        <span>3 / 17 Lakeside Pde Budgewoi<br>NSW 2262 <strong>(By Appointment)</strong></span>
      </div>
      <div class="contact-item"><span>ABN 12 345 678 901</span></div>
    </div>
    <hr class="contact-rule">
    <div class="contact-web">
      <div class="email">
        <svg width="12" height="9" viewBox="0 0 12 9"><rect x="0.5" y="0.5" width="11" height="8" fill="none" stroke="var(--paper)"/><path d="M0.5 0.5 L6 5 L11.5 0.5" fill="none" stroke="var(--paper)"/></svg>
        info@btlaccounting.com.au
      </div>
      <div class="url">www.<strong>btlaccounting</strong>.com.au</div>
    </div>
  </div>
</section>

</body>
</html>
```